Business Coaching Model and Flow Chart

We need this flowchart, attached, to be updated in a modern and engaging way. This flowchart is the cornerstone of a business coaching class we are running, and will be the main support reference for the people who take the class. We are open to ideas as to how it is presented, but we would like a largely minimalist look that leaves space to be impactful where the key information sites. Our colour scheme is primary red (D51C29), white, grey (333333), black, and secondary green (3C8740). We will also need our logo present (attached).

```html
<!DOCTYPE html>
<html lang="en">
<head>
<meta charset="utf-8">
<title>Group to Teams – Through Learning Together</title>
<link rel="stylesheet" href="https://fonts.googleapis.com/css2?family=Oswald:wght@500;600;700&family=Pathway+Gothic+One&display=swap">
<style>
:root{
  --red:#d51c29;
  --green:#3c8740;
  --grey:#333333;
  --chip:#ececec;
  --white:#ffffff;
  --soft:rgba(0,0,0,.14);
}
*{box-sizing:border-box;margin:0;padding:0}
html,body{width:1200px;height:501px;overflow:hidden}
body{
  position:relative;
  background:radial-gradient(ellipse at 50% 40%,#ffffff 0%,#f7f7f7 60%,#efefef 100%);
  font-family:"Pathway Gothic One","Arial Narrow",sans-serif;
  color:var(--grey);
}
.brand{
  position:absolute;left:26px;top:26px;display:flex;align-items:center;gap:8px;
  font-family:"Oswald","Arial Narrow",sans-serif;font-weight:600;font-size:15px;color:var(--grey);letter-spacing:.3px;
}
.brand-mark{width:20px;height:20px;background:var(--red);border-radius:3px}
.title{
  position:absolute;left:6px;width:1200px;text-align:center;
  font-family:"Oswald","Arial Narrow",sans-serif;font-weight:700;color:var(--grey);
}
.title-main{top:20px;font-size:50px;line-height:58px;letter-spacing:.5px}
.title-sub{top:77px;font-size:27px;line-height:30px}
.stage-arrows{position:absolute;left:0;top:0}
.stage-label{
  position:absolute;top:127px;height:37px;display:flex;align-items:center;justify-content:center;
  text-align:center;color:var(--white);font-family:"Oswald","Arial Narrow",sans-serif;font-weight:600;
  font-size:12px;line-height:13px;text-transform:uppercase;letter-spacing:.2px;white-space:nowrap;
}
.stage-label.big{font-weight:700;font-size:29px;line-height:30px}
.item{
  position:absolute;display:flex;align-items:center;color:var(--white);
  font-size:13.5px;line-height:13px;border-radius:4px;white-space:nowrap;
  box-shadow:0 2px 3px var(--soft);
}
.item.red{background:var(--red);padding-left:34px}
.item.green{background:var(--green);padding-left:7px}
.item.center{justify-content:center;padding-left:0;text-align:center}
.item.topic{background:var(--chip);color:var(--grey);padding-left:18px;font-size:13px;box-shadow:0 1px 2px var(--soft)}
.item.topic::before{content:"";position:absolute;left:8px;top:50%;width:5px;height:5px;margin-top:-3px;border-radius:50%;background:var(--grey)}
.item.topic.tall{align-items:flex-start;padding-top:4px;line-height:12px}
.item.topic.tall::before{top:8px;margin-top:0}
.item.large{font-size:14.5px;line-height:15px}
.icon{position:absolute;left:8px;top:50%;width:20px;height:20px;margin-top:-10px}
.sol{padding-left:42px}
.sol .icon{left:10px}
</style>
</head>
<body>

<div class="brand"><span class="brand-mark"></span>Teamwise Coaching</div>

<h1 class="title title-main">GROUP TO TEAMS</h1>
<h2 class="title title-sub">THROUGH LEARNING TOGETHER</h2>

<svg class="stage-arrows" width="1200" height="501" viewBox="0 0 1200 501" aria-hidden="true">
  <g fill="#333333">
    <path d="M30,127 H158 V120 L189,145.5 L158,171 V164 H30 Q26,164 26,160 V131 Q26,127 30,127Z"/>
    <path d="M203,127 H322 V120 L352,145.5 L322,171 V164 H203 Q199,164 199,160 V131 Q199,127 203,127Z"/>
    <path d="M366,127 H495 V120 L526,145.5 L495,171 V164 H366 Q362,164 362,160 V131 Q362,127 366,127Z"/>
    <path d="M538,127 H642 V120 L672,145.5 L642,171 V164 H538 Q534,164 534,160 V131 Q534,127 538,127Z"/>
    <path d="M687,127 H805 V120 L835,145.5 L805,171 V164 H687 Q683,164 683,160 V131 Q683,127 687,127Z"/>
    <path d="M847,127 H990 V120 L1021,145.5 L990,171 V164 H847 Q843,164 843,160 V131 Q843,127 847,127Z"/>
    <rect x="1029" y="127" width="151" height="37" rx="4"/>
  </g>
</svg>

<div class="stage-label big" style="left:26px;width:142px">PROBLEM</div>
<div class="stage-label" style="left:199px;width:127px">Clarify challenges<br>diagnostics</div>
<div class="stage-label" style="left:362px;width:140px">Planning for success<br>make a plan</div>
<div class="stage-label" style="left:534px;width:112px">Learn the tools<br>workshops</div>
<div class="stage-label" style="left:683px;width:130px">Doing<br>mastering the tools</div>
<div class="stage-label" style="left:843px;width:150px">Reflect - Adapt - Embed</div>
<div class="stage-label big" style="left:1029px;width:151px">SOLUTION</div>

<!-- Problem -->
<div class="item red" style="left:26px;top:184px;width:137px;height:28px"><svg class="icon" viewBox="0 0 20 20"><rect x="4" y="2" width="12" height="16" rx="1" fill="#fff"/><path d="M7 7h6M7 10h6M7 13h4" stroke="#d51c29" stroke-width="1.5"/></svg>Underbilling</div>
<div class="item red" style="left:26px;top:218px;width:137px;height:28px"><svg class="icon" viewBox="0 0 20 20" fill="#fff"><circle cx="10" cy="6" r="3.5"/><circle cx="4" cy="8" r="2.5"/><circle cx="16" cy="8" r="2.5"/><path d="M4 18c0-5 12-5 12 0z"/></svg>Staff Retention</div>
<div class="item red" style="left:26px;top:252px;width:137px;height:28px"><svg class="icon" viewBox="0 0 20 20" fill="none" stroke="#fff" stroke-width="2"><circle cx="8" cy="8" r="6"/><path d="M12.5 12.5L18 18"/></svg>Hard to Recruit</div>
<div class="item red" style="left:26px;top:285px;width:137px;height:28px"><svg class="icon" viewBox="0 0 20 20"><path d="M2 3h16v11H11l-3 4v-4H2z" fill="#fff"/><path d="M10 5v5M10 11.5v1.5" stroke="#d51c29" stroke-width="2"/></svg>Client Complaints</div>
<div class="item red" style="left:26px;top:319px;width:137px;height:28px"><svg class="icon" viewBox="0 0 20 20"><circle cx="10" cy="10" r="8.5" fill="#fff"/></svg>Staff Stress &amp; Burnout</div>
<div class="item red" style="left:26px;top:353px;width:137px;height:28px;font-size:14.5px"><svg class="icon" viewBox="0 0 20 20" stroke="#fff" stroke-width="1.6"><path d="M10 1v6M10 13v6M1 10h6M13 10h6M4 4l4 4M12 12l4 4M16 4l-4 4M4 16l4-4"/></svg>Conflict</div>
<div class="item red" style="left:26px;top:387px;width:137px;height:28px"><svg class="icon" viewBox="0 0 20 20" fill="#fff"><path d="M2 8h10V4l6 5H2zM18 12H8v4l-6-5h16z"/></svg>FSS Constant Change</div>
<div class="item red" style="left:26px;top:421px;width:137px;height:28px"><svg class="icon" viewBox="0 0 20 20" fill="#fff"><path d="M4 2h12v2l-5 6 5 6v2H4v-2l5-6-5-6z"/></svg>Limited in Best Practice</div>

<!-- Diagnostics -->
<div class="item green" style="left:197px;top:184px;width:118px;height:22px">Scoping</div>
<div class="item green" style="left:197px;top:211px;width:118px;height:22px">Interviews</div>
<div class="item green" style="left:197px;top:239px;width:118px;height:22px">Group Reflection</div>
<div class="item green" style="left:197px;top:266px;width:118px;height:22px">Opinion Surveys</div>
<div class="item green" style="left:197px;top:293px;width:118px;height:22px">Certified Assessments</div>
<div class="item topic" style="left:197px;top:321px;width:118px;height:20px">Personality Styles</div>
<div class="item topic" style="left:197px;top:348px;width:118px;height:20px">Work Preference</div>
<div class="item topic" style="left:197px;top:375px;width:118px;height:20px">Strengths &amp; Values</div>
<div class="item topic" style="left:197px;top:403px;width:118px;height:20px">Trust</div>
<div class="item topic" style="left:197px;top:429px;width:118px;height:20px">360</div>

<!-- Plan -->
<div class="item green large" style="left:361px;top:184px;width:131px;height:38px;padding-left:8px">Team data Analysis<br>Workshop</div>
<div class="item green large" style="left:361px;top:229px;width:131px;height:37px;padding-left:8px">Individual<br>Development Plan</div>
<div class="item green large" style="left:361px;top:273px;width:131px;height:27px;padding-left:8px">Team Development Plan</div>
<div class="item green large" style="left:361px;top:306px;width:131px;height:27px;padding-left:8px">Organisational Plan</div>

<!-- Workshops -->
<div class="item green center large" style="left:532px;top:185px;width:125px;height:21px">Foundation Workshops</div>
<div class="item topic" style="left:532px;top:212px;width:125px;height:20px">Difficult Conversations</div>
<div class="item topic tall" style="left:532px;top:238px;width:125px;height:32px">Giving &amp; Recieving<br>feedback</div>
<div class="item topic" style="left:532px;top:275px;width:125px;height:20px">Values Alignment</div>
<div class="item topic" style="left:532px;top:299px;width:125px;height:20px">Shared Purpose</div>
<div class="item topic" style="left:532px;top:325px;width:125px;height:20px">Ways of working</div>
<div class="item topic" style="left:532px;top:349px;width:125px;height:20px">Diversity</div>
<div class="item topic" style="left:532px;top:374px;width:125px;height:20px">Wellbeing</div>
<div class="item topic" style="left:532px;top:399px;width:125px;height:20px">Time</div>
<div class="item green center large" style="left:532px;top:425px;width:125px;height:24px">Customized Workshops</div>

<!-- Doing -->
<div class="item green center large" style="left:682px;top:185px;width:126px;height:27px">Group Coaching</div>
<div class="item green center large" style="left:682px;top:244px;width:126px;height:27px">Team Coaching</div>
<div class="item green center large" style="left:682px;top:303px;width:126px;height:27px">Individual Coaching</div>
<div class="item green center large" style="left:682px;top:363px;width:126px;height:27px">Peer Learning</div>
<div class="item green center large" style="left:682px;top:423px;width:126px;height:27px">Lunch n Learn</div>

<!-- Embed -->
<div class="item green center" style="left:845px;top:184px;width:148px;height:21px">Culture Committee</div>
<div class="item green center" style="left:845px;top:209px;width:148px;height:21px">Embedding Workshop</div>
<div class="item green center" style="left:845px;top:233px;width:148px;height:21px">Culture Collateral</div>
<div class="item green center" style="left:845px;top:258px;width:148px;height:21px">WOW Manifesto</div>
<div class="item green center" style="left:845px;top:283px;width:148px;height:21px">Leadership Team Coaching</div>
<div class="item green center" style="left:845px;top:307px;width:148px;height:21px">Measure ROI</div>
<div class="item green center" style="left:845px;top:332px;width:148px;height:21px">Evaluation Survey</div>
<div class="item green center" style="left:845px;top:356px;width:148px;height:21px">Temprature Checks</div>
<div class="item green center" style="left:845px;top:381px;width:148px;height:21px">Recruit to Suit</div>
<div class="item green center" style="left:845px;top:405px;width:148px;height:21px">Future Proofing - What’s Next</div>
<div class="item green center" style="left:845px;top:430px;width:148px;height:21px">Evaluation Survey</div>

<!-- Solution -->
<div class="item red large sol" style="left:1030px;top:183px;width:153px;height:38px"><svg class="icon" viewBox="0 0 20 20" fill="#fff"><circle cx="10" cy="6" r="4.5"/><path d="M2 19c0-8 16-8 16 0z"/></svg>Self Awareness<br>&amp; Ownership</div>
<div class="item red large sol" style="left:1030px;top:225px;width:153px;height:26px"><svg class="icon" viewBox="0 0 24 20" fill="#fff"><path d="M1 6l5-3 6 4 6-4 5 3-4 6-7 5-7-5z"/></svg>Partnership</div>
<div class="item red large sol" style="left:1030px;top:255px;width:153px;height:30px"><svg class="icon" viewBox="0 0 20 20" fill="#fff"><circle cx="10" cy="3" r="2.5"/><rect x="7" y="6" width="6" height="5"/><rect x="2" y="11" width="16" height="8"/></svg>Great Place to work</div>
<div class="item red large sol" style="left:1030px;top:290px;width:153px;height:27px"><svg class="icon" viewBox="0 0 20 20" fill="#fff"><path d="M10 12C6 10 3 8 3 3c4 0 7 3 7 9zM10 12c4-2 7-4 7-9-4 0-7 3-7 9zM2 14h11l5 2-5 3H2z"/></svg>Growth Mindset</div>
<div class="item red large sol" style="left:1030px;top:321px;width:153px;height:30px"><svg class="icon" viewBox="0 0 20 20" fill="#fff"><path d="M2 7h4l10-5v16L6 13H2zM5 13l2 6h3l-2-6z"/></svg>Coach Approach<br>Culture</div>
<div class="item red large sol" style="left:1030px;top:355px;width:153px;height:26px"><svg class="icon" style="left:7px;width:28px" viewBox="0 0 28 20"><rect x="1" y="3" width="26" height="13" rx="2" fill="#fff"/><path d="M7 6l1 2.5h2.5l-2 1.5 1 2.5L7 11l-2.5 1.5 1-2.5-2-1.5H6zM14 6l1 2.5h2.5l-2 1.5 1 2.5L14 11l-2.5 1.5 1-2.5-2-1.5H13zM21 6l1 2.5h2.5l-2 1.5 1 2.5L21 11l-2.5 1.5 1-2.5-2-1.5H20z" fill="#d51c29"/></svg>Feedback Culture</div>
<div class="item red large sol" style="left:1030px;top:384px;width:153px;height:32px"><svg class="icon" viewBox="0 0 20 20"><circle cx="9" cy="9" r="7" fill="none" stroke="#fff" stroke-width="3" stroke-dasharray="3 2"/><circle cx="9" cy="9" r="3" fill="#fff"/><path d="M12 12l6 6" stroke="#fff" stroke-width="2.5"/></svg>Way to manage<br>Conflict</div>
<div class="item red large sol" style="left:1030px;top:419px;width:153px;height:31px"><svg class="icon" viewBox="0 0 20 20"><path d="M1 2h18v12h-8l-4 4v-4H1z" fill="#fff"/><path d="M4 6h12M4 9h12M4 12h8" stroke="#d51c29" stroke-width="1.4"/></svg>Best practice<br>Communication skills</div>

</body>
</html>
```